Need Web Banners Designed for Mobile Banking App

We need a web banner designed to introduce the launch of our Mobile Banking App.

About our App:
Members can enjoy fast, easy and secure access to their accounts on the go. It’s the convenient way to manage your accounts, transfer funds, pay bills and more… no matter where you are!

Requirements:
We need 2 sizes of the Banner (no more than 300 dpi). Banners are to be the same design, we just need 2 different sizes.

Banner 1. 754px (width) x 209px (height)
Banner 2. 8 inches (wide) x 1.5 inches (height)

Colors to use: We like blues and find it goes well on our website but we don't have any color requirements.

Banner should contain the following:

- Headline Text:
We've always been local, now we're mobile.

- Sub-headline Text:
Introducing the HRF Mobile App for Zorbix and Pellmar.

- "Available on the app store" badge". See attached for example. Should not include the Vesko logo since our app is available for both Zorbix and Pellmar.

Attached is also a screen shot of the Mobile Banking App that the member will see when they log into their account. This can be used if it fits in with your design but it's optional.

```html
<!DOCTYPE html>
<html lang="en">
<head>
<meta charset="utf-8">
<title>HRF Mobile App Banner</title>
<link href="https://fonts.googleapis.com/css2?family=Arimo:wght@400;700&display=swap" rel="stylesheet">
<style>
  :root {
    --navy: #2c3a86;
    --bar-blue: #2f4e8a;
    --soft-blue: #5f82c2;
    --white: #ffffff;
    --panel: #f2f2f3;
    --store-green: #8cbc3c;
    --store-gray: #5a5a5e;
  }
  html, body {
    margin: 0;
    padding: 0;
    width: 1200px;
    height: 144px;
    overflow: hidden;
    background: var(--white);
  }
  .banner {
    position: relative;
    width: 1200px;
    height: 144px;
    font-family: "Arimo", Arial, sans-serif;
    overflow: hidden;
  }
  .hero {
    position: absolute;
    left: 0;
    top: 0;
    width: 1200px;
    height: 108px;
    background: linear-gradient(90deg,
      #5c84b8 0%,
      #67acbe 12%,
      #70b9b0 28%,
      #7ebf8e 48%,
      #a8bd92 62%,
      #c2b8a6 75%,
      #c9c3c4 88%,
      #cfcfd2 100%);
  }
  .headline {
    position: absolute;
    right: 37px;
    top: 38px;
    margin: 0;
    font-weight: 400;
    font-size: 38px;
    line-height: 1;
    color: var(--white);
    white-space: nowrap;
    letter-spacing: -0.2px;
  }
  .headline .accent-navy { color: var(--navy); }
  .headline .accent-blue { color: var(--soft-blue); }
  .info-bar {
    position: absolute;
    left: 0;
    top: 108px;
    width: 1200px;
    height: 36px;
    background: var(--bar-blue);
  }
  .subheadline {
    position: absolute;
    left: 20px;
    top: 9px;
    margin: 0;
    font-size: 18px;
    line-height: 1;
    color: var(--white);
    white-space: nowrap;
  }
  .availability {
    position: absolute;
    right: 85px;
    top: 9px;
    margin: 0;
    font-size: 18px;
    line-height: 1;
    color: var(--white);
    white-space: nowrap;
  }
  .store-panel {
    position: absolute;
    right: 0;
    top: 0;
    width: 78px;
    height: 36px;
    background: var(--panel);
    display: flex;
    flex-direction: column;
    align-items: flex-start;
    justify-content: center;
    gap: 3px;
    padding-left: 10px;
    box-sizing: border-box;
  }
  .store-name {
    display: flex;
    align-items: center;
    gap: 4px;
    font-size: 11px;
    font-weight: 700;
    line-height: 1;
  }
  .store-name .dot {
    width: 6px;
    height: 6px;
    border-radius: 50%;
  }
  .store-pellmar { color: var(--store-green); }
  .store-pellmar .dot { background: var(--store-green); }
  .store-zorbix { color: var(--store-gray); }
  .store-zorbix .dot { background: var(--store-gray); }
</style>
</head>
<body>
  <div class="banner">
    <div class="hero">
      <h1 class="headline">We've <span class="accent-navy">always</span> been local, now <span class="accent-blue">we're</span> <span class="accent-navy">mobile.</span></h1>
    </div>
    <div class="info-bar">
      <p class="subheadline">Introducing the HRF Mobile App for Zorbix and Pellmar.</p>
      <p class="availability">Available on</p>
      <div class="store-panel">
        <span class="store-name store-pellmar"><span class="dot"></span>Pellmar</span>
        <span class="store-name store-zorbix"><span class="dot"></span>Zorbix</span>
      </div>
    </div>
  </div>
</body>
</html>
```